Make a medical leaflet for my patients undergoing ankle blocks

I have a very boring text only leaflet I would like to turn into a professional appealing medical leaflet to give to my patients. I would like to get this onto two pages of a4 if possible and its intended for electronic distribution mainly.
This will be for patients so it must be professional.
It must also contain a copyright logo on it and my name near the start (Dr Tobias Wendell) so my colleagues can't use it easily.
Target Market(s)
Patients undergoing surgery
Industry/Entity Type
Medical
Font styles to use
Other font styles liked:
- no idea, you tell me
Requirements
Must have
- the information contained on the attachment
- look professional
- a copyright on it
Nice to have
- the ashbury clinic logo
Should not have
- Any spelling, grammatical or linguistic errors
- Any font less than size 12

```html
<!DOCTYPE html>
<html lang="en">
<head>
<meta charset="utf-8">
<title>Ankle Block – Patient Leaflet</title>
<link rel="stylesheet" href="https://fonts.googleapis.com/css2?family=Open+Sans:ital,wght@0,400;0,600;1,400&family=Fira+Sans+Condensed:wght@500;600&display=swap">
<style>
  :root{
    --navy:#1d3a5e;
    --blue:#2a5f97;
    --pale:#d5dee8;
    --ink:#1f3f66;
    --text:#2c3e55;
    --violet:#3d2f6e;
    --bg:#eeeeee;
    --white:#ffffff;
  }
  *{box-sizing:border-box;margin:0;padding:0}
  html,body{width:1200px;height:804px;overflow:hidden;background:var(--bg)}
  body{position:relative;font-family:"Open Sans",Arial,sans-serif;color:var(--text)}
  .page{position:absolute;top:74px;width:482px;height:682px;background:var(--white);overflow:hidden}
  .page--front{left:72px}
  .page--back{left:629px}
  .abs{position:absolute}
  .block{position:absolute}
  .navy{background:var(--navy)}
  .blue{background:var(--blue)}
  .pale{background:var(--pale)}
  .body-text{font-size:8.4px;line-height:11.5px;text-align:justify}
  .heading{font-family:"Fira Sans Condensed","Arial Narrow",sans-serif;font-weight:600;color:var(--ink);font-size:11.5px;line-height:14px}

  /* front page */
  .author{left:15px;top:22px;font-size:10px;font-weight:600;color:var(--ink);white-space:nowrap}
  .hospital-name{left:210px;top:18px;font-size:22px;color:var(--violet);white-space:nowrap}
  .group-name{left:234px;top:60px;font-size:12px;color:var(--blue);white-space:nowrap}
  .intro-panel{left:0;top:52px;width:182px;height:358px;background:var(--blue);color:var(--white)}
  .intro-title{left:15px;top:16px;font-family:"Fira Sans Condensed","Arial Narrow",sans-serif;font-weight:600;font-size:20px;line-height:24px;color:var(--white)}
  .intro-rule{left:15px;top:42px;width:152px;height:1px;background:var(--white)}
  .intro-text{left:15px;width:152px;color:var(--white)}
  .photo{left:182px;top:91px;width:300px;height:301px;background:radial-gradient(circle at 48% 40%,#c4433f 0,#6a3b46 7%,transparent 15%),radial-gradient(ellipse at 50% 50%,#8f9aa6 0,#3b4450 45%,#0f1419 90%)}
  .section-icon{width:18px;height:18px;background:var(--navy);border-radius:2px}
  .checklist{list-style:none;font-size:8.2px;line-height:11.4px}
  .checklist li::before{content:"☑";margin-right:4px}
  .pill{height:16px;border-radius:8px;background:var(--navy);color:var(--white);font-size:8px;font-weight:600;line-height:16px;padding:0 9px}
  .risk-list{font-size:6.5px;line-height:8.7px;padding-left:8px}
  .risk-list .plain{list-style:none}
  .note-box{left:278px;top:616px;width:204px;height:46px;background:var(--blue);color:var(--white);font-size:6.3px;line-height:8.5px;font-style:italic;padding:7px 10px 0 14px}

  /* back page */
  .copy{left:110px;width:350px}
  .indent{padding-left:18px;text-align:left}
  .clinic-name{left:236px;top:626px;font-size:12px;color:var(--white);white-space:nowrap}
  .clinic-square{left:222px;top:630px;width:9px;height:9px;background:var(--white)}
  .copyright{left:110px;top:660px;font-size:7px;color:var(--text);white-space:nowrap}
</style>
</head>
<body>

<!-- Page one -->
<section class="page page--front">
  <div class="abs author">Dr Tobias Wendell</div>
  <div class="abs hospital-name">Kingsgate Hospital</div>
  <div class="abs group-name">part of Meridian Health UK</div>

  <div class="abs intro-panel">
    <h1 class="abs intro-title">Ankle block</h1>
    <div class="abs intro-rule"></div>
    <p class="abs intro-text body-text" style="top:54px">You are scheduled to have surgery on your foot. It is my normal practice to offer and perform (with your consent) an ankle block. This is an optional injection of numbing liquid to the nerves which supply your foot. The ankle block can be performed when you are awake, sedated or under general anaesthesia.</p>
    <p class="abs intro-text body-text" style="top:170px">The ankle block can be combined with a general anaesthetic and with sedation. It can also be used to allow surgery to be performed with you wide awake in certain cases.</p>
    <p class="abs intro-text body-text" style="top:240px">Having or not having an ankle block does not change the pre operative fasting guidelines you have been given.<br>There is a fee for performing an ankle block. Please consult my initial introductory email and terms of business for detail.</p>
  </div>

  <div class="abs photo" role="img" aria-label="X-ray style photograph of a foot and ankle with the ankle joint glowing red"></div>

  <div class="block navy" style="left:182px;top:392px;width:32px;height:18px"></div>
  <div class="block blue" style="left:214px;top:289px;width:32px;height:32px"></div>
  <div class="block blue" style="left:346px;top:360px;width:34px;height:32px;opacity:.9"></div>
  <div class="block pale" style="left:380px;top:392px;width:66px;height:46px"></div>
  <div class="block blue" style="left:446px;top:358px;width:36px;height:52px"></div>
  <div class="block navy" style="left:0;top:410px;width:58px;height:272px"></div>
  <div class="block navy" style="left:64px;top:618px;width:14px;height:15px"></div>
  <div class="block pale" style="left:64px;top:633px;width:22px;height:29px"></div>
  <div class="block blue" style="left:48px;top:648px;width:16px;height:14px"></div>

  <div class="abs section-icon" style="left:68px;top:422px"></div>
  <h2 class="abs heading" style="left:94px;top:423px">What are the benefits</h2>
  <ul class="abs checklist" style="left:98px;top:438px">
    <li>Excellent pain relief - usually 10 - 14 hours (and rarely 24 - 48 hours)</li>
    <li>Avoiding traditional painkillers, resulting in less post operative nausea and vomiting</li>
    <li>The option to avoid a general anaesthetic (if you wish)</li>
    <li>A faster recovery from the general anaesthetic</li>
    <li>Certain surgery requires an overnight stay in hospital without an ankle block</li>
  </ul>

  <div class="abs section-icon" style="left:68px;top:500px"></div>
  <h2 class="abs heading" style="left:94px;top:501px">What are the risks?</h2>
  <p class="abs" style="left:96px;top:518px;font-size:8px;font-style:italic;font-weight:600;color:var(--ink)">As with all injections, there is the risk of bruising, bleeding and infection.</p>

  <div class="abs pill" style="left:88px;top:534px">Nerve Damage</div>
  <ul class="abs risk-list" style="left:92px;top:556px;width:174px">
    <li>Occurs 1 in 5000 nerve blocks.</li>
    <li>Creates an area of numbness or weakness/paralysis in some / all the foot.</li>
    <li>Majority of nerve injuries will heal themselves within a year.</li>
    <li>There is no treatment to fix it. If the block has not worn off after 72 hours please let me know.</li>
  </ul>

  <div class="abs pill" style="left:88px;top:622px">Failure</div>
  <ul class="abs risk-list" style="left:92px;top:643px;width:174px">
    <li>The success rate with ankle blocks is 98 - 99%.</li>
    <li>Some blocks will fail, partially or totally. If total failure,</li>
    <li>I will discuss repeating the block with your consent.</li>
  </ul>

  <div class="abs pill" style="left:282px;top:534px">Pain During Operation</div>
  <ul class="abs risk-list" style="left:280px;top:556px;width:178px">
    <li>If you choose to have wide awake surgery or surgery under sedation, the surgery will stop and I will discuss three options with you:</li>
    <li class="plain">- more numbing liquid to be injected by the surgeon</li>
    <li class="plain">- more sedation / painkiller</li>
    <li class="plain">- having a general anaesthetic</li>
  </ul>

  <p class="abs note-box">If you decide to undergo surgery awake or sedated, there is a risk you will need to have a general anaesthetic if you feel pain. This is why the starvation instructions of awake surgery and general anaesthesia are the same.</p>
</section>

<!-- Page two -->
<section class="page page--back">
  <div class="block navy" style="left:0;top:22px;width:42px;height:118px"></div>
  <div class="block blue" style="left:42px;top:29px;width:26px;height:26px"></div>
  <div class="block pale" style="left:42px;top:54px;width:52px;height:48px"></div>
  <div class="block blue" style="left:16px;top:80px;width:26px;height:22px;opacity:.85"></div>
  <div class="block blue" style="left:0;top:154px;width:82px;height:404px"></div>
  <div class="block navy" style="left:0;top:558px;width:82px;height:66px"></div>
  <div class="block blue" style="left:82px;top:562px;width:14px;height:14px"></div>
  <div class="block pale" style="left:82px;top:576px;width:28px;height:28px"></div>
  <div class="block navy" style="left:82px;top:605px;width:400px;height:50px"></div>
  <div class="block blue" style="left:0;top:624px;width:82px;height:58px"></div>

  <h2 class="abs heading" style="left:110px;top:44px">How is it done</h2>
  <p class="abs copy body-text" style="top:61px">Excellent pain relief - usually 10 - 14 hours (and rarely 24 - 48 hours). Avoiding traditional painkillers, resulting in less post operative nausea and vomiting. The option to avoid a general anaesthetic (if you wish). A faster recovery from the general anaesthetic.</p>

  <h2 class="abs heading" style="left:110px;top:124px">If you choose a General anaesthetic</h2>
  <p class="abs copy body-text indent" style="top:142px">I will perform the ankle block after I start the general anaesthetic.<br>You should wake up from your surgery with a comfortable and numb foot/feet.<br>If you wake in pain, we can repeat the ankle block or provide traditional painkillers.</p>
  <p class="abs copy body-text" style="top:184px">Whatever you choose, there will be a cannula placed in your hand and heart and oxygen monitoring throughout.</p>

  <h2 class="abs heading" style="left:110px;top:225px">After surgery</h2>
  <p class="abs copy body-text" style="top:242px">You will go to the recovery area and then onto the ward when you are ready. It will be difficult to walk while the block is working so physiotherapists will help you first walk. If you need crutches they will teach you how to use them.</p>
  <p class="abs copy body-text" style="top:288px">Your foot will be numb and so you will not feel where your foot is in relation to nearby objects. As a result, it is easy to knock your foot. Please take extra care while your foot is still numb.</p>
  <p class="abs copy body-text" style="top:333px">As the block wears off, the foot may feel slightly painful, tingly or hot. At this point you should take your painkillers I have prescribed. Depending on your medical history you will have up to three painkillers. I would suggest to start with all three. You will also have an anti - sickness prescribed if one of the painkillers (typically codeine or morphine) makes you feel sick.</p>
  <p class="abs copy body-text" style="top:401px">Occasionally (1 - 2%), pain when the block wears off will be severe. In this case contact your surgeon's secretary. We can use stronger pain medication, but there will be a charge in writing and getting the private prescription to you (please see my terms of business) via courier.</p>

  <h2 class="abs heading" style="left:110px;top:460px">The alternative</h2>
  <p class="abs copy body-text indent" style="top:478px">If you do not have an ankle block your surgery can still proceed.<br>Post operative pain can be managed with traditional painkillers.<br>However, you are more likely to need an overnight stay or feel sick after the anaesthetic.</p>
  <p class="abs copy body-text" style="top:532px">If you have any further questions about an ankle block I will see you the day of your surgery. Alternatively, you can request the following optional services (as mentioned in my terms of business).</p>

  <span class="abs clinic-square"></span>
  <span class="abs clinic-name">The Ashbury Clinic</span>
  <p class="abs copyright">© Dr Tobias Wendell. All rights reserved.</p>
</section>

</body>
</html>
```